Kids School Holiday Tennis Camp Flyer

We are a small tennis center based in Sydney's Eastern Suburbs - Australia.
We run coaching programs for kids and adults and also during school holidays organise fun tennis camps for kids aged 6-15 yrs.
Our website is www.brightvolleycourts.com but we dont necessarily need the flyer to tie in with the website design, although happy to have any advice on this.
We would like our logo on there and lots of bright kids colours .... especially yellow's (like tennis balls) and greens (like grass courts).
We would like to convey the message of fun, games, sunshine, interaction but also fitness and learning new tennis skills ..... so its not a play school but a true tennis camp. However - it is also fun to attend and meet other kids.
We would like a double sided flyer if possible with the next terms coaching advertised on the back.
Tennis camp dates to be listed :
Spring Tennis Camps WEEK 1 : Mon Sept 24th - Fri Sept 28th
WEEK 2: Tues Oct 2nd - Fri Oct 5th
Summer Tennis Camps WEEK 1 : Mon Jan 7th - Fri Jan 11th
WEEK 2: Mon Jan 14th - Fri Jan 18th
WEEK 3: Mon Jan 21st - Fri Jan 25th
Flip side of the flyer to advertise kids school term coaching:
Term 4 kids tennis is an 11 week terms, starts Monday October 8th and runs until Friday Dec 21st
Term 1 2013 is also an 11 week term running from Mon Jan 28th to Fri April 12th.
Target Market(s)
Its a kids tennis camp but the parents will be the buyer - so it must have a kids feel but also appeal to the mum and dads !
Industry/Entity Type
Fitness
Look and feel

```html
<!DOCTYPE html>
<html lang="en">
<head>
<meta charset="utf-8">
<title>Tennis Camp Flyer</title>
<link rel="stylesheet" href="https://fonts.googleapis.com/css2?family=Oswald:wght@400;500&family=Kaushan+Script&display=swap">
<style>
  :root {
    --page: #ffffff;
    --green: #5db52c;
    --green-dark: #3f8f1a;
    --green-light: #a6d94a;
    --ball: #e6f02a;
    --ink: #3b3b3b;
    --sky-top: #bcd4ee;
    --sky-mid: #e3edf8;
    --sky-low: #f6f9fc;
    --seat-red: #c8363a;
    --seat-blue: #2e4f9c;
    --label: #4a4a4a;
  }
  * { margin: 0; padding: 0; box-sizing: border-box; }
  html, body { width: 800px; height: 1200px; overflow: hidden; background: var(--page); }
  body { position: relative; font-family: 'Oswald', sans-serif; color: var(--ink); }

  .flyer {
    position: absolute; top: 22px; width: 375px; height: 562px; overflow: hidden;
    background: linear-gradient(180deg, var(--sky-top) 0%, var(--sky-mid) 40%, var(--sky-low) 75%, #ffffff 100%);
    box-shadow: 0 1px 4px rgba(0,0,0,.25);
  }
  .flyer--front { left: 17px; }
  .flyer--back { left: 408px; }
  .abs { position: absolute; }

  .brand {
    position: absolute; top: 12px; right: 12px; display: flex; align-items: center; gap: 4px;
    font-size: 11px; font-weight: 500; color: var(--green); text-transform: lowercase; line-height: 1;
  }
  .brand__dot { width: 8px; height: 8px; border-radius: 50%; background: var(--ball); }

  .photo-kids {
    left: 10px; top: 30px; width: 345px; height: 290px;
    background: linear-gradient(90deg, #4c7fc2 0%, #4c7fc2 26%, #2c2c32 40%, #2c2c32 60%, #83b352 72%, #6d6a66 100%);
    -webkit-mask-image: linear-gradient(180deg, rgba(0,0,0,0) 0%, rgba(0,0,0,.55) 25%, #000 60%);
    mask-image: linear-gradient(180deg, rgba(0,0,0,0) 0%, rgba(0,0,0,.55) 25%, #000 60%);
    border-radius: 60px 60px 0 0;
    opacity: .9;
  }
  .photo-seats {
    left: 0; width: 375px; height: 48px;
    background:
      repeating-linear-gradient(180deg, rgba(255,255,255,.18) 0 2px, rgba(0,0,0,0) 2px 6px),
      linear-gradient(90deg, var(--seat-red) 0%, var(--seat-blue) 20%, var(--seat-blue) 48%, var(--seat-red) 52%, var(--seat-red) 75%, var(--seat-blue) 90%);
  }
  .banner { left: 14px; top: 288px; width: 347px; height: 68px; }
  .banner__title {
    position: absolute; left: 0; right: 0; top: 299px; text-align: center;
    font-size: 42px; font-weight: 500; color: #fff; letter-spacing: 0.5px; line-height: 1;
    text-shadow: 0 2px 2px rgba(0,0,0,.3);
  }

  .heading {
    position: absolute; left: 16px; right: 16px; display: flex; align-items: center; gap: 8px;
    color: var(--green); font-size: 14px; font-weight: 500; text-transform: uppercase; line-height: 1;
  }
  .heading::before, .heading::after { content: ""; flex: 1; height: 1.5px; background: var(--green); }
  .line {
    position: absolute; left: 0; right: 0; text-align: center; text-transform: uppercase;
    font-size: 10.5px; line-height: 1; color: var(--ink); white-space: nowrap;
  }
  .footer {
    position: absolute; left: 0; right: 0; bottom: 0; height: 14px; background: var(--green);
    display: flex; justify-content: space-between; align-items: center; padding: 0 8px;
    font-size: 6.5px; color: #fff; text-transform: uppercase; letter-spacing: .2px;
  }

  .back-title {
    position: absolute; left: 0; right: 0; top: 28px; text-align: center;
    font-size: 26px; font-weight: 500; color: var(--green); text-transform: uppercase; line-height: 1;
  }
  .back-intro { font-size: 11px; }
  .term-big { font-size: 14px; }
  .photo-kid {
    -webkit-mask-image: linear-gradient(180deg, rgba(0,0,0,0) 0%, #000 30%);
    mask-image: linear-gradient(180deg, rgba(0,0,0,0) 0%, #000 30%);
    border-radius: 40px 40px 0 0;
  }
  .photo-kid-left { left: 0; top: 300px; width: 92px; height: 262px; background: linear-gradient(180deg, #b9a08a 0%, #86b25a 35%, #86b25a 70%, #6a6a6a 100%); }
  .photo-kid-right { left: 258px; top: 326px; width: 117px; height: 236px; background: linear-gradient(180deg, #c9a98a 0%, #2f2f34 45%, #2f2f34 78%, #3c4a66 100%); }

  .side-label {
    position: absolute; top: 600px; font-family: 'Kaushan Script', cursive; font-size: 32px; color: var(--label);
  }
</style>
</head>
<body>

  <section class="flyer flyer--front">
    <div class="abs photo-kids" role="img" aria-label="Photo of three kids holding tennis rackets"></div>
    <div class="brand"><span class="brand__dot"></span>bright volley courts</div>

    <svg class="abs banner" viewBox="0 0 347 68" aria-hidden="true">
      <polygon points="0,22 40,22 40,62 0,62 14,42" fill="var(--green-dark)"/>
      <polygon points="347,22 307,22 307,62 347,62 333,42" fill="var(--green-dark)"/>
      <rect x="30" y="8" width="287" height="50" fill="var(--green)"/>
      <rect x="30" y="8" width="287" height="22" fill="var(--green-light)" opacity=".45"/>
      <circle cx="298" cy="14" r="9" fill="var(--ball)"/>
      <path d="M291,9 q7,5 14,0 M291,19 q7,-5 14,0" stroke="#fff" stroke-width="1" fill="none"/>
    </svg>
    <div class="banner__title">TENNIS CAMP</div>

    <div class="heading" style="top:376px">Spring Tennis Camp</div>
    <div class="line" style="top:398px">Week 1 : Mon Sept 24th - Fri Sept 28th | Week 2: Tues Oct 2nd - Fri Oct 5th</div>
    <div class="heading" style="top:424px">Summer Tennis Camp</div>
    <div class="line" style="top:446px">Week 1 : Mon Jan 7th - Fri Jan 11th | Week 2: Mon Jan 14th - Fri Jan 18th</div>
    <div class="line" style="top:466px">Week 3: Mon Jan 21st - Fri Jan 25th</div>

    <div class="abs photo-seats" style="top:500px" role="img" aria-label="Photo of red and blue stadium seats"></div>
    <div class="footer">
      <span>www.brightvolleycourts.com</span>
      <span>facebook.com/brightvolley</span>
      <span>12 Harbour Lane, Clovelly NSW 2031</span>
      <span>9000 1234</span>
    </div>
  </section>

  <section class="flyer flyer--back">
    <div class="back-title">Kids School Term Coaching</div>
    <div class="line back-intro" style="top:66px">At Bright Volley Courts we are committed to delivering</div>
    <div class="line back-intro" style="top:84px">a positive tennis experience no matter what your level.</div>

    <div class="heading" style="top:135px">Term 4 Kids Tennis</div>
    <div class="line term-big" style="top:162px">11 Week Terms</div>
    <div class="line" style="top:183px">Mon October 8th and runs until Fri Dec 21st</div>

    <div class="heading" style="top:220px">Term 1 2013</div>
    <div class="line term-big" style="top:240px">11 Week Term</div>
    <div class="line" style="top:262px">From Mon Jan 28th to Fri April 12th</div>

    <div class="abs photo-seats" style="top:500px; height:62px" role="img" aria-label="Photo of red and blue stadium seats"></div>
    <div class="abs photo-kid photo-kid-left" role="img" aria-label="Photo of a boy holding a tennis racket"></div>
    <div class="abs photo-kid photo-kid-right" role="img" aria-label="Photo of a girl holding a tennis racket"></div>
  </section>

  <div class="side-label" style="left:165px">front</div>
  <div class="side-label" style="left:540px">back</div>

</body>
</html>
```